Brightmoor Learning Brochure Design Project

Our company requires a brochure for promoting our Corporate Training business.

Please use data from Corporate training brochure doc.
Updates

Dear Designers,

We have added new corporate brochure document into the project. Use this data to finish up your brochure.

Thanks,

Omar Kasprzak

Reason: We have recently finalised the data that will go into the corporate brochure.

Reason: To get more better designs

Target Market(s)

Training Managers / Business Managers / Hiring Managers

Industry/Entity Type

Training

Requirements
Must have
• Corporate and Professional Look

```html
<!DOCTYPE html>
<html lang="en">
<head>
<meta charset="utf-8">
<title>Brightmoor Learning — Corporate Training Brochure</title>
<link rel="stylesheet" href="https://fonts.googleapis.com/css2?family=Source+Sans+3:wght@300;400;600;700&display=swap">
<style>
:root{
  --frame-purple:#3b1a4d;
  --frame-purple-dark:#2a0f38;
  --frame-white:#ffffff;
  --panel:#3a3a3a;
  --panel-mid:#363636;
  --nav:#383838;
  --tab-top:#5a5a5a;
  --tab-bottom:#444444;
  --rule:#555555;
  --text:#ffffff;
  --text-muted:#a9a9a9;
  --link:#7fb8e0;
  --photo-a:#6b6f74;
  --photo-b:#8c9096;
}
*{margin:0;padding:0;box-sizing:border-box}
html,body{width:1200px;height:933px;overflow:hidden}
body{
  background:radial-gradient(ellipse at center,var(--frame-purple),var(--frame-purple-dark));
  font-family:"Source Sans 3",Arial,sans-serif;
  color:var(--text);
}
.sheet{
  position:absolute;left:0;top:0;width:1013px;height:788px;
  transform-origin:0 0;transform:scale(1.1846,1.184);
}
.frame{position:absolute;left:8px;top:8px;width:997px;height:772px;background:var(--frame-white)}
.brochure{position:absolute;left:22px;top:22px;width:968px;height:743px;background:var(--panel);outline:1px solid #888}
.nav{position:absolute;left:0;top:0;width:968px;height:92px;background:var(--nav)}
.nav-tab{position:absolute;top:0;width:162px;height:92px;
  background:linear-gradient(var(--tab-top),var(--tab-bottom));padding:34px 0 0 25px}
.nav-title{font-size:14px;font-weight:700;line-height:14px;letter-spacing:-.2px}
.nav-sub{font-size:12.5px;color:var(--text-muted);line-height:14px}
.nav-arrow{position:absolute;right:6px;bottom:6px;width:10px;height:10px}
.col-mid{position:absolute;left:321px;top:92px;width:332px;height:433px;background:var(--panel-mid)}
.photo{position:absolute;background:linear-gradient(160deg,var(--photo-b),var(--photo-a))}
h2{position:absolute;font-weight:300;font-size:28px;line-height:32px;letter-spacing:-.3px;white-space:nowrap}
.copy{position:absolute;font-size:12.4px;line-height:15px}
.copy b{font-weight:700}
.item{position:absolute;left:346px;width:300px;height:70px}
.thumb{position:absolute;left:0;top:0;width:70px;height:69px;border:1px solid #777;
  background:linear-gradient(150deg,#b5b7ba,#6d7074)}
.item .copy{left:81px;top:0;width:218px}
.item a{color:var(--link)}
.muted{color:var(--text-muted)}
.bottom-rule{position:absolute;left:0;top:525px;width:968px;height:1px;background:var(--rule)}
</style>
</head>
<body>
<div class="sheet">
  <div class="frame"></div>
  <div class="brochure">
    <nav class="nav">
      <div class="nav-tab" style="left:0">
        <div class="nav-title">OUR SERVICES</div><div class="nav-sub">our main services</div>
        <svg class="nav-arrow" viewBox="0 0 10 10"><path d="M1 1L8 8M8 3V8H3" stroke="#9a9a9a" stroke-width="1.4" fill="none"/></svg>
      </div>
      <div class="nav-tab" style="left:321px">
        <div class="nav-title">SOLUTIONS</div><div class="nav-sub">the best solution</div>
        <svg class="nav-arrow" viewBox="0 0 10 10"><path d="M1 1L8 8M8 3V8H3" stroke="#9a9a9a" stroke-width="1.4" fill="none"/></svg>
      </div>
      <div class="nav-tab" style="left:653px">
        <div class="nav-title">OUR GOAL</div><div class="nav-sub">goal achievement</div>
        <svg class="nav-arrow" viewBox="0 0 10 10"><path d="M1 1L8 8M8 3V8H3" stroke="#9a9a9a" stroke-width="1.4" fill="none"/></svg>
      </div>
    </nav>

    <div class="col-mid"></div>

    <!-- Overview -->
    <div class="photo" role="img" aria-label="Business people reviewing work on a laptop" style="left:20px;top:113px;width:143px;height:200px"></div>
    <h2 style="left:178px;top:106px">Overview</h2>
    <p class="copy" style="left:178px;top:143px;width:135px"><b>Quisque nulla.</b> Lorem ipsum dolor sit amet, consectetur adipisicing elit, sed do eiusmod tempor incididunt ut labore et dolore magna aliqua. Ut enim ad minim veniam, quis nostrud exercitation ullamco laboris nisi ut aliquip ex ea commodo</p>

    <h2 style="left:22px;top:320px">Feature</h2>
    <p class="copy" style="left:20px;top:358px;width:290px"><b>Quisque nulla.</b> Lorem ipsum dolor sit amet, con-sectetur adipisicing elit, sed do eiusmod tempor incididunt ut labore et dolore magna aliqua. Ut enim ad minim veniam, quis nostrud exercitation ullamco laboris nisi ut aliquip ex ea commodo consequat. Duis aute irure dolor in reprehenderit in voluptate velit esse cillum dolore eu fugiat nulla pariatur. Excepteur sint occaecat cupidatat non proident, sunt in culpa qui officia deserunt mollit anim id est laborum</p>

    <!-- Business Training -->
    <h2 style="left:345px;top:106px">Bussiness Training</h2>
    <div class="item" style="top:150px">
      <div class="thumb" role="img" aria-label="Team meeting around a table"></div>
      <p class="copy"><a>Corporate.</a> Vestibulum ante ipsum primis in fauibus sed orci luctus et ultrices posuere cubilia disse sollicitu-din. <span class="muted">velit sed leo. Ut pharetra augue nec augue. Nam elit magna, hendrerit</span></p>
    </div>
    <div class="item" style="top:242px">
      <div class="thumb" role="img" aria-label="Managers in discussion"></div>
      <p class="copy"><a>Management.</a> Vestibulum ante ipsum primis in fauibus sed orci luctus et ultrices posuere cubilia disse sollicitu-din. <span class="muted">velit sed leo. Ut pharetra augue nec augue. Nam elit magna, hendrerit</span></p>
    </div>
    <div class="item" style="top:336px">
      <div class="thumb" role="img" aria-label="Trainer working with a colleague"></div>
      <p class="copy"><a>Training.</a> Vestibulum ante ipsum primis in fauibus sed orci luctus et ultrices posuere cubilia disse sollicitudin. <span class="muted">velit sed leo. Ut pharetra augue nec augue. Nam elit magna, hendrerit sit amet,</span></p>
    </div>
    <div class="item" style="top:429px">
      <div class="thumb" role="img" aria-label="Professional on a phone call"></div>
      <p class="copy"><a>Solutions.</a> Vestibulum ante ipsum primis in fauibus sed orci luctus et ultrices posuere cubilia disse sollicitu-din. <span class="muted">velit sed leo. Ut pharetra augue nec augue. Nam elit magna, hendrerit</span></p>
    </div>

    <!-- Training Goal -->
    <h2 style="left:673px;top:108px">Training Goal</h2>
    <div class="photo" role="img" aria-label="Cheering business team seen from above" style="left:654px;top:146px;width:314px;height:167px;background:linear-gradient(160deg,#7d8a96,#4f5a64)"></div>
    <p class="copy" style="left:672px;top:337px;width:280px"><b>Quisque nulla.</b> Lorem ipsum dolor sit amet, con-sectetur adipisicing elit, sed do eiusmod tempor incididunt ut labore et dolore magna aliqua. Ut enim ad minim veniam, quis nostrud exercitation ullamco laboris nisi ut aliquip ex ea commodo consequat. Duis aute irure dolor in reprehenderit in voluptate velit esse cillum dolore eu fugiat nulla pariatur. Excepteur sint occaecat cupidatat non proident, sunt in culpa qui officia deserunt mollit anim id est laborum</p>

    <div class="bottom-rule"></div>

    <!-- We Offer Solutions -->
    <div class="photo" role="img" aria-label="Celebrating business team with raised arms" style="left:0;top:526px;width:321px;height:217px;background:linear-gradient(160deg,#9a9488,#55524c)"></div>
    <h2 style="left:348px;top:536px">We Offer Solutions</h2>
    <p class="copy" style="left:345px;top:576px;width:285px"><b>Quisque nulla.</b> Lorem ipsum dolor sit amet, con-sectetur adipisicing elit, sed do eiusmod tempor incididunt ut labore et dolore magna aliqua. Ut enim ad minim veniam, quis nostrud exercitation ullamco laboris nisi ut aliquip ex ea commodo consequat. Duis aute irure dolor in reprehenderit in voluptate velit esse cillum dolore eu fugiat nulla pariatur. Excepteur sint occaecat cupidatat non proident, sunt in culpa qui officia deserunt mollit anim id est laborum</p>

    <div class="photo" role="img" aria-label="Two businessmen celebrating outside an office building" style="left:675px;top:538px;width:136px;height:192px;background:linear-gradient(170deg,#c9ccd0,#55585c)"></div>
    <p class="copy" style="left:826px;top:538px;width:135px"><b>Quisque nulla.</b> Lorem ipsum dolor sit amet, consectetur adipisicing elit, sed do eiusmod tempor incididunt ut labore et dolore magna aliqua. Ut enim ad minim veniam, quis nostrud exercitation ullamco laboris nisi ut aliquip ex ea commodo consequat. Duis aute irure dolor in reprehen-</p>
  </div>
</div>
</body>
</html>
```